Unique Concept Design to Website Needed

Please see the attached folder. I have random images,etc but most importantly I have an attached image I was working on as a concept of a website. The brown background with blue and brown squares. logo in upper left and a little about me and then the squares would have names on them to lead to a section of the website with more info. I envision, when you mouse over a square, an image would appear so I attached random images here as well. Maybe some squares already have some images too.
- I want simple fonts. i like CLEAN, fonts
- text should be minimal. i am changing my site to less text, more powerful, bolder, larger lines with less content
- i am not sold on brown as the secondary color. i like blue but maybe grays, whites, offwhite scales or some other colors
-i have another graphic in there too
-you can see from my mock what company i am. please feel free to look me up and pull any portfolio , info , etc content to help make a great mock.
Do something cool!

```html
<!DOCTYPE html>
<html lang="en">
<head>
<meta charset="utf-8">
<title>Swift Web Studio</title>
<link href="https://fonts.googleapis.com/css2?family=Didact+Gothic&family=Arimo:wght@400;700&display=swap" rel="stylesheet">
<style>
  :root{
    --sage-light:#e6ebdd;
    --sage:#cdd6c1;
    --sage-dark:#aab59d;
    --navy:#1f3552;
    --ink:#4a4f48;
    --blue:#45c0ea;
    --blue-deep:#2a8fb9;
    --blue-steel:#3d7f9e;
    --gray:#9a9a98;
    --gray-dark:#6d6e6c;
    --charcoal:#2a2a28;
    --pale:#e7ebe0;
    --white:#ffffff;
    --olive:#8e8a2c;
    --umber:#3a2a14;
  }
  *{box-sizing:border-box;margin:0;padding:0}
  html,body{width:1200px;height:819px;overflow:hidden}
  body{position:relative;font-family:"Arimo",Arial,sans-serif;background:var(--sage)}
  .backdrop{position:absolute;inset:0;background:linear-gradient(120deg,var(--sage-light) 0%,var(--sage) 45%,var(--sage-dark) 100%)}
  .brand{position:absolute;left:34px;top:52px;display:flex;align-items:center;gap:12px;
    font-family:"Didact Gothic",sans-serif;font-size:34px;line-height:1;color:var(--navy);white-space:nowrap}
  .brand-mark{width:26px;height:26px;background:var(--navy)}
  .intro{position:absolute;left:136px;top:185px;font-family:"Didact Gothic",sans-serif;font-size:15px;
    line-height:21px;letter-spacing:.35px;color:var(--ink);white-space:nowrap}
  .top-nav{position:absolute;right:52px;top:12px;display:flex;gap:18px;align-items:center}
  .top-nav svg{display:block}
  .tile{position:absolute;overflow:hidden;
    background-image:linear-gradient(var(--line,rgba(255,255,255,.55)) 0 0),linear-gradient(var(--line,rgba(255,255,255,.55)) 0 0);
    background-size:1.5px 100%,100% 1.5px;background-position:50% 0,0 50%;background-repeat:no-repeat}
  .plain{background-image:none}
  .blue{background-color:var(--blue)}
  .blue-deep{background-color:var(--blue-deep)}
  .steel{background-color:var(--blue-steel)}
  .white{background-color:var(--white)}
  .gray{background-color:var(--gray)}
  .gray-dark{background-color:var(--gray-dark)}
  .charcoal{background-color:var(--charcoal)}
  .pale{background-color:var(--pale);opacity:.92}
  .label{position:absolute;color:var(--white);font-size:15px;line-height:19px;white-space:nowrap}
  .label.dark{color:#5a5e57;font-size:16px;line-height:21px;text-align:center;width:100%;left:0}
  .label.bold{font-weight:700;font-size:16px;line-height:20px}
  .photo{position:absolute}
  .social-cell{position:absolute;width:52px;height:52px;border:2px solid var(--white);border-radius:4px}
  .play{position:absolute;left:40px;top:22px;width:48px;height:48px;border:2px solid var(--white)}
</style>
</head>
<body>
  <div class="backdrop" role="img" aria-label="Softly washed photo of a bright office with a consultant at his desk"></div>

  <div class="brand">
    <span class="brand-mark"></span>
    <span class="brand-name">Swift Web Studio</span>
  </div>

  <p class="intro">Daniel Moreno is a digital marketing<br>consultant developing and promoting websites ,<br>digital media and videos, for businesses</p>

  <nav class="top-nav" aria-label="Quick links">
    <svg width="38" height="34" viewBox="0 0 38 34" aria-label="home"><path d="M2 17 19 3l17 14" fill="none" stroke="#000" stroke-width="4"/><path d="M8 15v17h8v-9h6v9h8V15" fill="#000"/></svg>
    <svg width="40" height="34" viewBox="0 0 40 34" aria-label="contact"><path d="M4 3c3-2 6 0 7 3s0 5-2 6c1 5 4 9 9 11 1-2 3-3 5-2s4 4 2 7c-2 3-7 3-12-1S3 16 2 10C2 6 2 4 4 3z" fill="#000"/><rect x="17" y="6" width="21" height="14" fill="#fff" stroke="#000" stroke-width="2"/><path d="M17 6l10.5 8L38 6" fill="none" stroke="#000" stroke-width="2"/></svg>
    <svg width="18" height="34" viewBox="0 0 18 34" aria-label="location"><path d="M9 1a8 8 0 0 0-8 8c0 7 8 16 8 24 0-8 8-17 8-24a8 8 0 0 0-8-8z" fill="#000"/><circle cx="9" cy="9" r="3" fill="#fff"/></svg>
  </nav>

  <!-- upper mosaic -->
  <div class="tile white plain" style="left:431px;top:102px;width:56px;height:60px;border-radius:0 0 0 22px"></div>
  <div class="tile blue plain" style="left:460px;top:135px;width:28px;height:28px"></div>
  <div class="tile white plain" style="left:493px;top:135px;width:56px;height:30px;border-radius:22px 0 0 0"></div>
  <div class="tile white plain" style="left:553px;top:135px;width:56px;height:30px;border-radius:0 22px 0 0"></div>
  <div class="tile white" style="left:493px;top:170px;width:116px;height:100px;border-radius:0 0 0 40px"></div>
  <div class="tile blue plain" style="left:553px;top:170px;width:55px;height:30px"></div>
  <div class="tile white" style="left:620px;top:78px;width:111px;height:124px;border-radius:40px 0 0 0"></div>
  <div class="tile blue" style="left:613px;top:206px;width:118px;height:129px;border-radius:0 0 0 40px"></div>
  <span class="label" style="left:672px;top:293px">services</span>
  <div class="tile blue" style="left:736px;top:78px;width:110px;height:117px;border-radius:40px 40px 0 40px"></div>
  <span class="label" style="left:741px;top:153px">design</span>
  <div class="tile gray" style="left:850px;top:108px;width:116px;height:88px;border-radius:0 36px 0 0"></div>
  <div class="tile gray" style="left:971px;top:108px;width:60px;height:60px;border-radius:0 24px 0 0"></div>
  <div class="tile gray-dark plain" style="left:1032px;top:136px;width:56px;height:60px;border-radius:24px 24px 0 0"></div>
  <div class="tile steel" style="left:736px;top:206px;width:230px;height:124px;border-radius:0 40px 0 0"></div>
  <span class="label" style="left:803px;top:282px">pay<br>online</span>
  <div class="tile blue-deep" style="left:969px;top:206px;width:121px;height:124px;border-radius:40px 0 0 0"></div>
  <span class="label" style="left:998px;top:228px">portfolio</span>

  <!-- left mosaic -->
  <div class="tile gray" style="left:215px;top:272px;width:112px;height:244px;border-radius:40px 0 0 0"></div>
  <div class="tile gray" style="left:330px;top:272px;width:110px;height:123px;border-radius:40px 40px 0 0"></div>
  <span class="label" style="left:397px;top:361px">blog</span>
  <div class="tile gray-dark" style="left:330px;top:398px;width:110px;height:118px;border-radius:0 0 0 40px"></div>
  <div class="tile blue-deep plain" style="left:270px;top:335px;width:56px;height:58px"></div>
  <div class="tile blue" style="left:443px;top:335px;width:107px;height:120px;border-radius:40px 0 40px 0"></div>
  <div class="tile blue-deep" style="left:443px;top:398px;width:107px;height:118px;border-radius:0 0 0 40px"></div>
  <span class="label" style="left:445px;top:480px">media</span>
  <div class="tile gray" style="left:553px;top:338px;width:115px;height:58px;border-radius:0 0 0 24px"></div>
  <div class="tile gray-dark" style="left:553px;top:400px;width:115px;height:62px;border-radius:20px 0 20px 0"></div>

  <!-- services group -->
  <div class="tile pale plain" style="left:733px;top:347px;width:114px;height:115px;border-radius:40px 0 0 0"><span class="label dark" style="top:40px">website<br>design</span></div>
  <div class="photo" style="left:850px;top:347px;width:115px;height:115px;border-radius:0 40px 0 0;background:linear-gradient(160deg,#e3c25a,#a4752f)" role="img" aria-label="Portrait photo of the consultant"></div>
  <div class="tile pale plain" style="left:733px;top:465px;width:114px;height:115px;border-radius:0 0 0 40px"><span class="label dark" style="top:27px">website<br>hosting</span></div>
  <div class="tile pale plain" style="left:850px;top:465px;width:115px;height:115px"><span class="label dark" style="top:29px">website<br>promotion</span></div>

  <div class="tile gray-dark" style="left:978px;top:337px;width:112px;height:123px;border-radius:0 40px 0 40px"></div>
  <span class="label" style="left:1008px;top:350px">free<br>resources</span>

  <div class="tile charcoal" style="left:975px;top:462px;width:115px;height:126px;border-radius:40px 0 40px 0;--line:rgba(255,255,255,.25)" aria-label="Social links">
    <span class="social-cell" style="left:8px;top:8px"></span>
    <span class="social-cell" style="left:58px;top:8px"></span>
    <span class="social-cell" style="left:8px;top:66px"></span>
    <span class="social-cell" style="left:58px;top:66px"></span>
  </div>

  <!-- media block -->
  <div class="photo" style="left:217px;top:523px;width:110px;height:112px;border-radius:40px 0 0 0;background:linear-gradient(140deg,#c8c24a,var(--olive))" role="img" aria-label="Video still of the office street front">
    <span class="play"><svg width="44" height="44" viewBox="0 0 44 44"><path d="M15 11l16 11-16 11z" fill="#fff"/></svg></span>
  </div>
  <div class="photo" style="left:330px;top:523px;width:110px;height:112px;border-radius:0 0 40px 0;background:linear-gradient(140deg,#4a3a18,var(--umber))" role="img" aria-label="Photo of the office interior">
    <span class="label bold" style="left:16px;top:46px">about us</span>
  </div>
  <div class="photo" style="left:217px;top:638px;width:110px;height:110px;background:linear-gradient(150deg,#5d5722,#2f2c12)" role="img" aria-label="Photo of the owner's desk">
    <span class="label bold" style="left:0;width:100%;text-align:center;top:34px">from the<br>owner</span>
  </div>
  <div class="tile charcoal plain" style="left:330px;top:638px;width:110px;height:110px;border-radius:40px 0 0 0;background-color:#111">
    <span class="label bold" style="left:3px;top:40px">testimonials</span>
  </div>
</body>
</html>
```